Wheels 4 Hire Car Co-Hosting program

I want to create an ad on Pictora, graphic design with my company name is Wheels 4 Hire . I am a host on the Vexa platform and I rent my cars out.
I have 90+ cars..
I’m trying to reach people that Have an extra car laying around or just tired of their car but are stuck with the payments.
And tell them Unlock earning potential with your car!
List it on our fleet for hassle-free renting on Vexa.
We manage A-Z and you profit.
Start now!
Dm us year, make, model and current mileage on odometer to find out if you qualify!
Vehicle must have a clean title and must be registered to you!

Target Market(s)

People that have an extra car laying around or are tired of their car and warm to get into a new car but they are stuck with the payments of their original car. We can take their car and rent it out for them.

Industry/Entity Type

Car rental fleet management

Requirements
Must have
• Car rental, money, profit, etc

```html
<!DOCTYPE html>
<html lang="en">
<head>
<meta charset="utf-8">
<title>Wheels 4 Hire – Car Co-Hosting</title>
<link rel="stylesheet" href="https://fonts.googleapis.com/css2?family=Krona+One&family=Lexend:wght@500;600;800;900&family=Figtree:wght@700;800&display=swap">
<style>
  :root {
    --black: #000000;
    --maroon: #3b0406;
    --white: #ffffff;
    --red: #e8141b;
    --lot-light: #3c3d40;
    --lot-dark: #17181a;
  }
  html, body {
    margin: 0;
    padding: 0;
    overflow: hidden;
    background: var(--black);
  }
  .ad {
    position: relative;
    width: 1200px;
    height: 1200px;
    overflow: hidden;
    background: var(--black);
    color: var(--white);
    text-align: center;
  }
  .ad__upper {
    position: absolute;
    left: 0; top: 0;
    width: 1200px; height: 800px;
    background: linear-gradient(to bottom, var(--black) 0%, #140102 35%, var(--maroon) 100%);
  }
  .ad__lot-photo {
    position: absolute;
    left: 0; top: 800px;
    width: 1200px; height: 400px;
    background: linear-gradient(to bottom, var(--lot-light) 0%, #26272a 50%, var(--lot-dark) 100%);
  }
  .line {
    position: absolute;
    left: 0;
    width: 1200px;
    margin: 0;
  }
  .brand-title {
    top: 38px;
    font-family: "Krona One", sans-serif;
    font-size: 104px;
    line-height: 120px;
    letter-spacing: 2px;
    color: var(--white);
  }
  .lead-caps {
    font-family: "Lexend", sans-serif;
    font-weight: 600;
    font-size: 30px;
    line-height: 40px;
    text-transform: uppercase;
    letter-spacing: -0.3px;
  }
  .lead-caps--offer { top: 213px; }
  .pitch {
    font-family: "Figtree", sans-serif;
    font-weight: 800;
    font-size: 37px;
    line-height: 46px;
  }
  .pitch--manage { top: 350px; }
  .pitch--relax { top: 410px; font-size: 50px; line-height: 60px; }
  .pitch--profits { top: 472px; }
  .cta-qualify {
    top: 560px;
    font-family: "Lexend", sans-serif;
    font-weight: 600;
    font-size: 41px;
    line-height: 48px;
    color: var(--red);
    text-transform: uppercase;
    letter-spacing: -0.5px;
  }
  .icon {
    position: absolute;
    fill: none;
    stroke: var(--white);
    stroke-width: 5;
    stroke-linejoin: round;
    stroke-linecap: round;
  }
  .icon--cash { left: 48px; top: 580px; width: 232px; height: 200px; }
  .icon--chat { left: 533px; top: 640px; width: 134px; height: 132px; }
  .icon--bag { left: 965px; top: 592px; width: 170px; height: 188px; }
  .lead-caps--title { top: 822px; font-size: 36px; line-height: 45px; }
  .lead-caps--machine { top: 972px; font-size: 33px; line-height: 42px; }
  .today {
    top: 1048px;
    font-family: "Lexend", sans-serif;
    font-weight: 900;
    font-size: 128px;
    line-height: 140px;
    color: var(--red);
    letter-spacing: -5px;
  }
</style>
</head>
<body>
<main class="ad">
  <div class="ad__upper"></div>
  <div class="ad__lot-photo" role="img" aria-label="Aerial view of a parking lot filled with rows of cars, darkened"></div>

  <h1 class="line brand-title">WHEELS 4 HIRE</h1>

  <p class="line lead-caps lead-caps--offer">List your car on our fleet for<br>hassle-free renting on Vexa.</p>

  <p class="line pitch pitch--manage">We manage everything from A to Z, so you can sit back,</p>
  <p class="line pitch pitch--relax">relax,</p>
  <p class="line pitch pitch--profits">and watch the profits roll in.</p>

  <p class="line cta-qualify">DM us to see if you qualify!</p>

  <svg class="icon icon--cash" viewBox="0 0 232 200" aria-hidden="true">
    <path d="M10 70 L130 10 L222 110 L102 170 Z"/>
    <path d="M10 70 L10 92 L102 192 L222 132 L222 110"/>
    <path d="M10 81 L102 181 L222 121"/>
    <path d="M62 44 L85 33 L177 133 L154 144 Z"/>
    <path d="M40 74 L118 35"/>
    <path d="M112 146 L190 107"/>
  </svg>

  <svg class="icon icon--chat" viewBox="0 0 134 132" aria-hidden="true">
    <path d="M4 4 H130 V96 H48 L26 126 V96 H4 Z"/>
    <path d="M34 36 H100 M34 50 H100 M34 64 H100"/>
  </svg>

  <svg class="icon icon--bag" viewBox="0 0 170 188" aria-hidden="true">
    <path d="M64 52 C40 20 52 8 70 16 C80 4 96 4 104 16 C122 8 130 24 108 52"/>
    <path d="M64 52 H108"/>
    <path d="M64 58 C20 90 6 140 18 166 C30 186 140 186 152 166 C164 140 150 90 108 58"/>
    <path d="M100 104 C96 94 70 94 70 110 C70 126 104 120 104 138 C104 154 74 154 68 142"/>
    <path d="M86 86 V162"/>
  </svg>

  <p class="line lead-caps lead-caps--title">Your vehicle must have a clean<br>title and be registered to you.</p>

  <p class="line lead-caps lead-caps--machine">Turn your car into a<br>money-making machine</p>
  <p class="line today">TODAY!</p>
</main>
</body>
</html>
```